VRB (Mirela Dovanski Wellness) Website supporting women to live a healthy lifestyle

Hi
I'm thrilled to be working together to bring a fresh look to my website! As an Integrative Health Practitioner, my mission is to support and empower women on their journey to reclaim their health and well-being. The website should feel inviting, with a soft and nurturing energy that also radiates vibrancy and vitality.

Design & Aesthetic:

I'd love to focus on rich rose gold tones
It should feel soft and approachable yet energetic and lively.

Functional Needs:

The site will support both my coaching services
and product sales, so it’s essential to have an intuitive and user-friendly shopping experience.
I'd love some exciting interactive features that keep visitors engaged and make the journey through the site feel seamless and uplifting.

Please let me know if there’s any additional information you need from me to bring this vision to life!

Thank you for your attention to these details! Here are some ideas I like to see Layout Ideas

Hero Section: An inviting header with a subtle half-moon background for a touch of healing energy.

Navigation & Logo: Place my logo in gold on the top left and use simple navigation links with a rose gold hover effect.

Section Dividers: Use small celestial icons, like a crescent moon, as dividers to create flow and add a bit of magic.

Product & Service Section: A soft rose gold gradient background to highlight products, with circular or wave accents around images.

Footer: Deep rose gold background with a half-moon icon to end with a warm invitation to connect.

Uploading an AI-generated image (it is a bit over the top but it captures the feel I like), with a hint of spirituality and femininity, along with elements like the half moon and colors. :) I'm also uploading my logos, and I have each option available in both color schemes.

Best,
Mirela

Industry/Entity Type

Health, Wellness

Coding

Coded - Design and coding required

Number of Pages Required

5+ page

Font styles to use
Other font styles liked:
• Playfair Display (Headings) & Lora (Body Text)

Requirements
Must have
• Shopify

```html
<!DOCTYPE html>
<html lang="en">
<head>
<meta charset="utf-8">
<title>VRB — Mirela Dovanski Wellness</title>
<link href="https://fonts.googleapis.com/css2?family=Cinzel:wght@400;500&family=Lora:ital,wght@0,400;1,400&family=Poppins:wght@400;500&family=Great+Vibes&display=swap" rel="stylesheet">
<style>
  :root{
    --rose:#e7b8a2;
    --rose-deep:#d89c82;
    --rose-soft:#f5ddd1;
    --rose-line:#e9c6b6;
    --ink:#2f2f31;
    --text:#6d6d70;
    --muted:#9a9a9e;
    --white:#ffffff;
    --hero-a:#2b2c30;
    --hero-b:#55575c;
  }
  *{margin:0;padding:0;box-sizing:border-box}
  html,body{width:1200px;height:3908px;overflow:hidden;background:var(--white)}
  body{position:relative;font-family:"Lora",serif;color:var(--text)}
  .abs{position:absolute}

  /* hero */
  .hero{left:0;top:0;width:1200px;height:560px;
    background:radial-gradient(ellipse at 62% 36%,#6c6c70 0%,rgba(86,86,90,.55) 24%,transparent 50%),linear-gradient(180deg,var(--hero-a),var(--hero-b) 70%,#3d3e42)}
  .brand{left:60px;top:26px;display:flex;align-items:center;gap:12px}
  .brand-dot{width:42px;height:42px;border-radius:50%;border:1.5px solid var(--rose)}
  .brand-name{font-family:"Cinzel",serif;color:var(--rose);font-size:15px;letter-spacing:2px;line-height:1.2}
  .nav{right:60px;top:38px;display:flex;gap:28px;font-family:"Poppins",sans-serif;font-size:13px;color:var(--white)}
  .nav span:first-child{color:var(--rose)}
  .hero-kicker{left:0;width:1200px;top:160px;text-align:center;color:#e8e2de;font-family:"Cinzel",serif;font-size:26px;letter-spacing:6px}
  .hero-title{left:0;width:1200px;top:196px;text-align:center;color:var(--white);font-family:"Cinzel",serif;font-weight:400;font-size:86px;letter-spacing:4px;line-height:1}
  .hero-copy{left:300px;width:600px;top:300px;text-align:center;color:#e2ddda;font-size:13px;line-height:1.7}

  /* service cards */
  .card{width:302px;height:330px;background:var(--white);box-shadow:0 6px 24px rgba(0,0,0,.12);top:458px}
  .card .photo{position:absolute;left:0;top:0;width:100%;height:170px}
  .card h3{position:absolute;top:192px;width:100%;text-align:center;font-family:"Poppins",sans-serif;font-weight:500;font-size:16px;color:var(--ink)}
  .card p{position:absolute;top:222px;left:40px;right:40px;text-align:center;font-size:12px;line-height:1.6;color:var(--muted)}
  .btn{display:inline-block;border:1px solid var(--rose-deep);color:var(--rose-deep);font-family:"Poppins",sans-serif;font-size:10px;letter-spacing:1.5px;padding:7px 16px;text-transform:uppercase}
  .card .btn{position:absolute;top:278px;left:50%;transform:translateX(-50%)}
  .card.feature .photo{height:330px}
  .card.feature .veil{position:absolute;inset:0;background:linear-gradient(180deg,rgba(30,30,32,.25),rgba(30,30,32,.75))}
  .card.feature h3{top:150px;color:var(--white)}
  .card.feature p{top:180px;color:#e6e0dc}
  .card.feature .btn{top:250px;background:var(--rose-deep);color:var(--white)}

  .rule{height:1px;background:var(--rose-line)}
  .divider-mark{width:14px;height:14px;border-radius:50%;background:var(--white);border:1.5px solid var(--rose-deep)}

  /* about */
  .about-head{left:60px;top:896px;display:flex;align-items:center;gap:18px}
  .about-head i{display:block;width:100px;height:1px;background:var(--rose-deep)}
  .about-head h2{font-family:"Cinzel",serif;font-weight:400;font-size:32px;color:var(--ink);letter-spacing:2px}
  .about-copy{left:180px;top:952px;width:340px;font-size:12px;line-height:1.75;color:var(--muted)}
  .about-copy p+p{margin-top:14px}
  .signature{font-family:"Great Vibes",cursive;color:var(--ink)}
  .about-ring{left:560px;top:870px;width:250px;height:250px;border-radius:50%;border:2px solid #f6e6de}
  .about-photo{left:745px;top:850px;width:380px;height:270px;background:radial-gradient(circle at 50% 40%,#c7785a 0%,#a8573d 30%,#efe7e3 62%,#f7f2ef)}

  /* nurturing */
  .nurture-photo{left:180px;top:1218px;width:420px;height:330px;background:linear-gradient(160deg,#1f4a3e,#2f6a55 45%,#8c2a22 70%,#1d3b32)}
  .nurture-box{left:555px;top:1282px;width:425px;height:360px;background:var(--rose);padding:70px 60px}
  .nurture-box h2{font-family:"Cinzel",serif;font-weight:400;font-size:34px;line-height:1.15;color:var(--ink)}
  .nurture-box p{margin-top:20px;font-size:12px;line-height:1.75;color:#5b4a43}
  .nurture-box .btn{margin-top:26px;border-color:#6b5148;color:#6b5148}

  /* testimonial */
  .avatar{left:570px;top:1786px;width:60px;height:60px;border-radius:50%;background:linear-gradient(135deg,#b7a08c,#6e7a5d)}
  .quote-mark{left:300px;top:1820px;font-family:"Cinzel",serif;font-size:200px;color:#f3e4dc;line-height:1}
  .quote{left:300px;top:1876px;width:600px;text-align:center;font-style:italic;font-size:18px;line-height:1.8;color:#707074}
  .side-orn{top:1924px;display:flex;align-items:center;gap:10px}
  .side-orn i{display:block;width:90px;height:1px;background:var(--rose-line)}

  /* vibrancy */
  .vibrancy{left:0;top:2176px;width:1200px;height:552px;overflow:hidden;
    background:linear-gradient(180deg,#c9d3d8 0%,#a9b8bf 28%,#3f5b52 45%,#2f6a70 62%,#3b7d86 80%,#2c5f66)}
  .vibrancy .kicker{position:absolute;left:60px;top:336px;font-family:"Cinzel",serif;font-size:22px;letter-spacing:5px;color:var(--white)}
  .vibrancy .lead{position:absolute;left:60px;top:370px;width:290px;font-size:12px;line-height:1.6;color:#eef3f4}
  .vibrancy .big{position:absolute;left:0;width:1200px;top:416px;text-align:center;font-family:"Cinzel",serif;font-size:160px;letter-spacing:6px;color:var(--white);line-height:1}

  /* blogs */
  .blogs-title{left:0;width:1200px;top:2830px;text-align:center;font-family:"Cinzel",serif;font-weight:400;font-size:36px;letter-spacing:3px;color:var(--ink)}
  .blogs-sub{left:400px;width:400px;top:2886px;text-align:center;font-size:13px;line-height:1.7;color:var(--muted)}
  .blog{top:2968px;width:302px;height:262px;background:var(--white);box-shadow:0 6px 24px rgba(0,0,0,.1)}
  .blog .photo{position:absolute;left:0;top:0;width:100%;height:130px}
  .blog .band{position:absolute;left:0;top:118px;width:100%;height:12px;background:var(--rose)}
  .blog h3{position:absolute;top:148px;width:100%;text-align:center;font-family:"Poppins",sans-serif;font-weight:500;font-size:15px;color:var(--ink)}
  .blog p{position:absolute;top:174px;left:40px;right:40px;text-align:center;font-size:11px;line-height:1.6;color:var(--muted)}
  .blog .btn{position:absolute;top:218px;left:50%;transform:translateX(-50%);font-size:9px;padding:6px 14px}
  .view-all{left:480px;top:3296px;display:flex;align-items:center;gap:16px;font-family:"Poppins",sans-serif;font-size:13px;color:var(--ink)}
  .view-all i{display:block;width:60px;height:1px;background:var(--ink)}

  /* footer */
  .footer{left:0;top:3408px;width:1200px;height:500px;background:var(--rose);overflow:hidden}
  .footer-arc{left:-300px;top:60px;width:560px;height:560px;border-radius:50%;border:3px solid #f3d2c3}
  .footer-brand{left:0;width:1200px;top:60px;display:flex;flex-direction:column;align-items:center;gap:10px}
  .footer-brand .brand-dot{width:72px;height:72px;border-color:var(--white);border-width:2px}
  .footer-brand .brand-name{color:var(--white);font-size:16px}
  .footer-nav{left:0;width:1200px;top:196px;display:flex;justify-content:center;gap:30px;font-family:"Poppins",sans-serif;font-size:13px;color:var(--white)}
  .socials{left:0;width:1200px;top:236px;display:flex;justify-content:center;gap:16px}
  .socials i{display:block;width:22px;height:22px;border-radius:50%;border:1.5px solid var(--white)}
  .copyright{left:0;width:1200px;top:284px;text-align:center;font-family:"Poppins",sans-serif;font-size:11px;color:#fff6f1}
</style>
</head>
<body>

<!-- HERO -->
<section class="abs hero" role="img" aria-label="Night sky with a glowing crescent moon over soft clouds"></section>
<div class="abs brand"><span class="brand-dot"></span><span class="brand-name">VRB<br>Mirela Dovanski</span></div>
<nav class="abs nav"><span>Home</span><span>About</span><span>Services</span><span>Blog</span><span>Contact</span></nav>
<div class="abs hero-kicker">Integrative Health</div>
<h1 class="abs hero-title">WELL-BEING</h1>
<p class="abs hero-copy">As an Integrative Health Practitioner, my mission is to support and empower women on their journey to reclaim their health and well-being with care.</p>

<div class="abs card" style="left:118px">
  <div class="photo" role="img" aria-label="Portrait photo of a smiling woman" style="background:linear-gradient(135deg,#c9b3a2,#8e7464)"></div>
  <h3>Integrative Health</h3>
  <p>Gentle guidance for body and mind, shaped around your own needs.</p>
  <span class="btn">Read More</span>
</div>
<div class="abs card feature" style="left:449px">
  <div class="photo" role="img" aria-label="Photo of a woman with long hair outdoors" style="background:linear-gradient(150deg,#6d5a4c,#3c3530)"></div>
  <div class="veil"></div>
  <h3>Empower Women</h3>
  <p>Support and tools that help you reclaim energy and balance every day.</p>
  <span class="btn">Read More</span>
</div>
<div class="abs card" style="left:780px">
  <div class="photo" role="img" aria-label="Portrait photo of a woman in warm light" style="background:linear-gradient(135deg,#d7b49a,#9a6e52)"></div>
  <h3>Journey of Life</h3>
  <p>Small steady changes that lead to a calm and vibrant lifestyle.</p>
  <span class="btn">Read More</span>
</div>

<!-- ABOUT -->
<div class="abs about-ring"></div>
<div class="abs about-head"><i></i><h2>ABOUT ME</h2></div>
<div class="abs about-copy">
  <p>I help women return to feeling rested, strong and at home in their bodies. My work blends nutrition, gentle movement and mindful habits into one clear plan.</p>
  <p>Every session is warm, personal and paced to fit real life.</p>
</div>
<div class="abs signature" style="left:180px;top:1060px;font-size:40px">Mirela</div>
<div class="abs about-photo" role="img" aria-label="Portrait photo of the practitioner smiling, wearing black"></div>

<div class="abs rule" style="left:60px;top:1140px;width:1080px"></div>
<div class="abs divider-mark" style="left:593px;top:1133px"></div>

<!-- NURTURING -->
<div class="abs nurture-photo" role="img" aria-label="Photo of a woman in a red dress among green ferns"></div>
<div class="abs nurture-box">
  <h2>NURTURING<br>ENERGY</h2>
  <p>Care that meets you where you are. Together we build rituals that restore calm, lift energy and bring lasting balance.</p>
  <span class="btn">Read More</span>
</div>

<div class="abs rule" style="left:60px;top:1690px;width:1080px"></div>
<div class="abs divider-mark" style="left:593px;top:1683px"></div>

<!-- TESTIMONIAL -->
<div class="abs quote-mark" aria-hidden="true">“</div>
<div class="abs avatar" role="img" aria-label="Small round photo of the client"></div>
<div class="abs side-orn" style="left:60px"><i></i><svg width="14" height="14" viewBox="0 0 14 14" aria-hidden="true"><circle cx="7" cy="7" r="4" fill="none" stroke="#d89c82"/></svg><i></i></div>
<div class="abs side-orn" style="left:928px"><i></i><svg width="14" height="14" viewBox="0 0 14 14" aria-hidden="true"><circle cx="7" cy="7" r="4" fill="none" stroke="#d89c82"/></svg><i></i></div>
<p class="abs quote">Lorem Ipsum is simply dummy text of the printing and typesetting industry. Lorem Ipsum has been the industry's standard dummy text ever since the 1500s, when an unknown printer took a galley</p>
<div class="abs signature" style="left:0;width:1200px;text-align:center;top:2010px;font-size:38px">Lena Hartwig</div>

<!-- VIBRANCY -->
<section class="abs vibrancy">
  <div class="abs" style="inset:0" role="img" aria-label="Photo of a woman from behind looking over a lake toward green hills"></div>
  <div class="kicker">Vitality</div>
  <p class="lead">As an Integrative Health Practitioner I bring energy and lightness to your days.</p>
  <div class="big">VIBRANCY</div>
</section>

<!-- BLOGS -->
<h2 class="abs blogs-title">BLOGS</h2>
<p class="abs blogs-sub">As an Integrative Health Practitioner I share notes, recipes and daily rituals.</p>

<div class="abs blog" style="left:118px">
  <div class="photo" role="img" aria-label="Photo of two women laughing together" style="background:linear-gradient(135deg,#d9b49c,#a6785e)"></div>
  <div class="band"></div>
  <h3>Integrative Health</h3>
  <p>Simple ideas for calmer mornings and better rest.</p>
  <span class="btn">Read More</span>
</div>
<div class="abs blog" style="left:449px">
  <div class="photo" role="img" aria-label="Photo of a woman on a sofa in a bright room" style="background:linear-gradient(135deg,#e3d7cd,#9f8b7c)"></div>
  <div class="band"></div>
  <h3>Integrative Health</h3>
  <p>How small habits build steady, lasting energy.</p>
  <span class="btn">Read More</span>
</div>
<div class="abs blog" style="left:780px">
  <div class="photo" role="img" aria-label="Photo of a smiling woman in golden light" style="background:linear-gradient(135deg,#e6c29a,#b07e52)"></div>
  <div class="band"></div>
  <h3>Integrative Health</h3>
  <p>Nourishing foods that support women's balance.</p>
  <span class="btn">Read More</span>
</div>
<div class="abs view-all"><i></i><span>View All Blogs</span></div>

<!-- FOOTER -->
<footer class="abs footer">
  <div class="abs footer-arc" aria-hidden="true"></div>
  <div class="abs footer-brand"><span class="brand-dot"></span><span class="brand-name">VRB</span></div>
  <nav class="abs footer-nav"><span>Home</span><span>About</span><span>Services</span><span>Blog</span><span>Contact</span></nav>
  <div class="abs socials"><i></i><i></i><i></i><i></i><i></i></div>
  <p class="abs copyright">© 2024 Mirela Dovanski Wellness. All rights reserved.</p>
</footer>

</body>
</html>
```